Label design for an exciting new Vodka brand

We need a label design for a dynamic new Vodka brand called 'Pale lantern Vodka'. It is a crisp and versatile liquid with a clean and smooth finish. It should appeal to 21-39 year olds, with a slight female skew. Colours, fonts and styles should be modern and relatively neutral - take inspiration from the brand pictures attached.

Target Market(s)

21-39 year olds, both male and female, but with a slight female skew

```html
<!DOCTYPE html>
<html lang="en">
<head>
<meta charset="utf-8">
<title>Pale lantern Vodka – Label</title>
<link href="https://fonts.googleapis.com/css2?family=Francois+One&family=Raleway:wght@500;700&display=swap" rel="stylesheet">
<style>
  :root {
    --page: #ffffff;
    --label: #ffffff;
    --orange: #e84e1c;
    --blue-mid: #1170b8;
    --blue-deep: #0b5aa0;
    --blue-soft: #93bde6;
    --ink: #0d0d0d;
    --volume: #a9c3d6;
    --bottle: #f2f2f2;
  }
  * { margin: 0; padding: 0; box-sizing: border-box; }
  html, body {
    width: 1200px;
    height: 1125px;
    overflow: hidden;
    background: var(--page);
  }
  .label {
    position: absolute;
    left: 342px;
    top: 200px;
    width: 558px;
    height: 742px;
    background: var(--label);
    box-shadow: 2px 2px 6px rgba(0,0,0,0.18);
    overflow: hidden;
  }
  .label-art {
    position: absolute;
    inset: 0;
    width: 558px;
    height: 742px;
  }
  .volume {
    position: absolute;
    left: 146px;
    top: 281px;
    font-family: 'Raleway', sans-serif;
    font-weight: 700;
    font-size: 21px;
    color: var(--volume);
  }
  .brand-name {
    position: absolute;
    left: 6px;
    top: 0;
    font-family: 'Francois One', sans-serif;
    font-weight: 400;
    color: var(--ink);
    line-height: 1;
  }
  .brand-line {
    position: absolute;
    left: 0;
    white-space: nowrap;
    letter-spacing: -1px;
  }
  .brand-line--first { top: 360px; font-size: 126px; }
  .brand-line--first .brand-small { font-size: 74px; margin-left: 10px; }
  .brand-line--second { top: 460px; font-size: 118px; }
  .description {
    position: absolute;
    left: 290px;
    top: 478px;
    width: 210px;
    font-family: 'Raleway', sans-serif;
    font-weight: 500;
    font-size: 10.5px;
    line-height: 15px;
    text-align: center;
    color: var(--ink);
  }
  .tagline {
    position: absolute;
    right: 36px;
    top: 692px;
    font-family: 'Raleway', sans-serif;
    font-weight: 700;
    font-size: 16px;
    line-height: 21px;
    text-align: right;
    color: var(--label);
  }
</style>
</head>
<body>
  <main class="label">
    <svg class="label-art" viewBox="0 0 558 742" xmlns="http://www.w3.org/2000/svg">
      <path class="wave-orange" fill="var(--orange)"
        d="M0 0 C40 20 70 38 108 40 C170 44 210 50 258 48 C330 44 370 30 408 28 C470 24 520 30 558 33 L558 100 L0 190 Z"/>
      <path class="wave-blue-mid" fill="var(--blue-mid)"
        d="M0 168 C60 160 110 150 153 146 C210 140 250 130 303 123 C360 115 410 106 453 100 C500 94 530 90 558 86 L558 260 L0 340 Z"/>
      <path class="wave-blue-deep" fill="var(--blue-deep)"
        d="M0 206 C80 200 160 218 250 210 C340 202 420 180 480 178 C520 177 540 180 558 183 L558 258 C480 262 400 270 333 280 C260 290 200 296 153 303 C90 312 40 325 0 340 Z"/>
      <circle class="badge-ring" cx="108" cy="123" r="56" fill="none" stroke="#f4f4f4" stroke-width="4"/>
      <rect class="bottle-art" x="70" y="100" width="56" height="110" rx="14" fill="var(--bottle)"
        transform="rotate(22 98 155)" role="img" aria-label="Illustration of a tilted vodka bottle"/>
      <rect class="bottle-art-small" x="94" y="254" width="44" height="40" rx="6" fill="var(--bottle)"
        transform="rotate(14 116 274)" role="img" aria-label="Illustration of a small glass"/>
      <path class="wave-soft" fill="var(--blue-soft)"
        d="M0 718 C50 705 100 692 153 685 C210 678 260 672 303 663 C340 655 365 642 393 633 C425 622 455 612 483 610 C515 608 540 612 558 618 L558 742 L0 742 Z"/>
    </svg>

    <div class="volume">500,ml</div>

    <h1 class="brand-name">
      <span class="brand-line brand-line--first">Pale<span class="brand-small">lantern</span></span>
      <span class="brand-line brand-line--second">Vodka</span>
    </h1>

    <p class="description">Lorem ipsum dolor sit amet, consectetuer adipiscing elit, sed diam Lorem ipsum dolor sit amet, consectetuer adipiscing elit, sed diam nonummy nibh euismod tincidunt ut laoreet dolore magna aliquam erat volutpat. Ut wisi enim ad minim veniam, quis nostrud</p>

    <p class="tagline">It is a crisp and versatile<br>liquid with a clean and smooth finish</p>
  </main>
</body>
</html>
```